Automated Invoicing of billable hours SAAS - Time management

I have an online Time Management SAAS: www.quelvano.com
I would like to have a new landing page explaining to the visitor that with Quelvano is very easy for a freelancer to invoice their billable hours for a given customer or project. Something like this page: https://www.quelvano.com/invoice-billable-hours
The page should explain to the visitor how easy the process is, that at the end of the billing interval, they don't have to go through some lists and calculate the billable hours, but Quelvano makes these all automatically. Also, mention the other extra features like someday tasks, reports, etc.
Maybe have a nice video with the entire process at the beginning of the page?
I want a page that will convert, a PRO version of the landing page mentioned above, both as design and marketing convincing value.
Please make the design with your graphics, and we will take care of the final pictures. What is essential for us is the content of the page, which sections are on it, what is the exact text, and we will change the graphics with our own, displaying the same content as you provide us in your design.
Look and feel
Each slider illustrates characteristics of the customer's brand and the style your logo design should communicate.

```html
<!DOCTYPE html>
<html lang="en">
<head>
<meta charset="UTF-8">
<title>Quelvano – Invoice Billable Hours</title>
<link href="https://fonts.googleapis.com/css2?family=Roboto:wght@400;500;700&display=swap" rel="stylesheet">
<style>
:root{
  --blue:#2a78d6;
  --blue-dark:#1f63b8;
  --green:#7bbf3e;
  --ink:#2b2f36;
  --muted:#7a7f87;
  --pale-blue:#eef5fd;
  --pale-green:#f2f9e8;
  --line:#e3e8ef;
  --white:#ffffff;
}
*{box-sizing:border-box;margin:0;padding:0}
html,body{width:1200px;height:5000px;overflow:hidden}
body{font-family:'Roboto',Arial,sans-serif;color:var(--ink);background:var(--white);position:relative}
a{color:inherit;text-decoration:none}

/* header */
.site-header{position:absolute;top:0;left:0;width:1200px;height:136px}
.brand{position:absolute;left:110px;top:42px;display:flex;align-items:center;gap:12px}
.brand-name{font-size:40px;font-weight:700;color:var(--blue);letter-spacing:.5px}
.brand-dot{width:30px;height:30px;border-radius:50%;background:var(--blue)}
.main-nav{position:absolute;left:431px;top:60px;display:flex;gap:36px;font-size:13px;font-weight:500;text-transform:uppercase;color:#3a3f47}
.btn{display:inline-flex;align-items:center;justify-content:center;font-size:13px;font-weight:700;text-transform:uppercase;color:var(--white);background:var(--green);border-radius:4px}
.btn-try{position:absolute;left:837px;top:45px;width:142px;height:48px}
.btn-login{position:absolute;left:988px;top:45px;width:100px;height:48px;background:var(--blue);gap:6px}

/* hero */
.hero{position:absolute;top:136px;left:0;width:1200px;height:508px;background:linear-gradient(180deg,#fff 0%,var(--pale-blue) 100%)}
.hero h1{position:absolute;left:110px;top:72px;font-size:40px;line-height:50px;font-weight:700;color:var(--blue);letter-spacing:1px}
.hero-list{position:absolute;left:110px;top:190px;list-style:none;font-size:20px;color:var(--ink)}
.hero-list li{display:flex;align-items:center;gap:18px;height:35px}
.hero-text{position:absolute;left:110px;top:270px;width:470px;font-size:16px;line-height:29px;color:#555}
.btn-hero{position:absolute;left:110px;top:351px;width:203px;height:45px}
.hero-art{position:absolute;left:612px;top:59px;width:476px;height:368px;border-radius:50% 50% 40% 40%/40% 40% 60% 60%;background:linear-gradient(160deg,#dbe9fa 0%,#c6dcf5 60%,#e9f2fc 100%)}

/* features */
.section-title{position:absolute;left:0;width:1200px;text-align:center;font-size:40px;font-weight:700;color:var(--blue);text-transform:uppercase}
.tabs{position:absolute;top:847px;left:359px;display:flex;gap:8px}
.tab{width:237px;height:48px;display:flex;align-items:center;justify-content:center;font-size:13px;font-weight:700;text-transform:uppercase;border-radius:3px}
.tab-active{background:var(--green);color:var(--white)}
.tab-idle{background:var(--white);color:var(--blue);box-shadow:0 4px 14px rgba(40,90,160,.15)}

.feature-title{position:absolute;font-size:32px;font-weight:700;color:var(--blue);text-transform:uppercase}
.feature-title::after{content:"";position:absolute;left:0;bottom:-10px;width:78px;height:4px;background:var(--green)}
.feature-sub{position:absolute;font-size:22px;font-weight:500;color:var(--ink)}
.feature-text{position:absolute;width:440px;font-size:15px;line-height:27px;color:var(--muted)}
.btn-more{position:absolute;width:131px;height:46px}

.blob{position:absolute;border-radius:50%}
.blob-blue{background:var(--pale-blue)}
.blob-green{background:var(--pale-green)}
.shot{position:absolute;background:linear-gradient(180deg,#fafcff 0%,#eef2f7 100%);border:1px solid var(--line);box-shadow:0 10px 30px rgba(30,60,110,.14);border-radius:3px}

/* to-do widget */
.todo{position:absolute;left:668px;top:1414px;width:284px;height:447px;background:var(--white);box-shadow:0 10px 30px rgba(30,60,110,.16);border:1px solid var(--line);font-size:12px}
.todo-head{height:34px;background:#eef2f7;display:flex;align-items:center;justify-content:space-between;padding:0 12px;font-size:14px;color:#444}
.todo-head span:last-child{color:var(--blue);font-size:11px}
.todo-item{position:relative;height:74px;border-bottom:1px solid var(--line);padding:5px 10px 0 14px;line-height:14px;color:#333}
.todo-item::before{content:"";position:absolute;left:3px;top:6px;bottom:6px;width:4px}
.todo-item b{font-weight:700}
.todo-item .chk{position:absolute;right:8px;top:8px;width:22px;height:22px;border:1px solid #cfd6e0;border-radius:3px}
.bar-red::before{background:#e2473c}.bar-orange::before{background:#f0a33a}.bar-green::before{background:#7bbf3e}.bar-blue::before{background:var(--blue)}
.pager{display:flex;justify-content:center;margin-top:10px}
.pager span{width:26px;height:26px;border:1px solid var(--line);display:flex;align-items:center;justify-content:center;color:var(--blue)}
.pager .on{background:var(--blue);color:var(--white)}

/* how it works */
.how{position:absolute;top:2894px;left:0;width:1200px;height:586px;background:var(--pale-blue)}
.how-card{position:absolute;top:175px;width:305px;height:334px;background:var(--white);box-shadow:0 6px 20px rgba(30,60,110,.08);text-align:center}
.how-icon{width:86px;height:86px;border-radius:50%;margin:38px auto 0;display:flex;align-items:center;justify-content:center}
.how-card h3{margin-top:40px;font-size:17px;font-weight:700;text-transform:uppercase}
.how-card p{margin:20px auto 0;width:262px;font-size:14px;line-height:26px;color:var(--muted)}

/* extra */
.extra-intro{position:absolute;left:140px;top:3670px;width:920px;text-align:center;font-size:15px;line-height:27px;font-weight:500;color:#4a4f57}
.extra-title{position:absolute;font-size:32px;font-weight:700;color:var(--ink);text-transform:uppercase}
.extra-text{position:absolute;width:440px;font-size:15px;line-height:27px;color:var(--muted)}
.art{position:absolute}

/* footer */
.site-footer{position:absolute;top:4716px;left:0;width:1200px;height:284px;background:var(--blue);color:var(--white)}
.foot-brand{position:absolute;left:110px;top:103px;display:flex;align-items:center;gap:10px}
.foot-brand .brand-name{color:var(--white);font-size:34px}
.foot-brand .brand-dot{background:var(--white);width:24px;height:24px}
.social{position:absolute;left:158px;top:162px;display:flex;gap:5px}
.social span{width:18px;height:18px;border-radius:50%;background:var(--green)}
.foot-col{position:absolute;top:56px}
.foot-col h4{font-size:15px;font-weight:500;text-transform:uppercase;letter-spacing:.3px;margin-bottom:18px}
.foot-col ul{list-style:none;font-size:13px}
.foot-col li{height:31px;display:flex;align-items:center;gap:14px}
.foot-col li::before{content:"";width:10px;height:10px;border-radius:50%;background:var(--green)}
.foot-rule{position:absolute;left:110px;top:236px;width:978px;height:1px;background:rgba(255,255,255,.35)}
.foot-bottom{position:absolute;top:251px;font-size:12px}
</style>
</head>
<body>

<header class="site-header">
  <a class="brand" href="#"><span class="brand-name">Quelvano</span><span class="brand-dot"></span></a>
  <nav class="main-nav">
    <a href="#">Resources &#8964;</a><a href="#">Customers</a><a href="#">Prices</a><a href="#">Contact</a>
  </nav>
  <a class="btn btn-try" href="#">Try it for free</a>
  <a class="btn btn-login" href="#">
    <svg width="11" height="12" viewBox="0 0 11 12"><circle cx="5.5" cy="3" r="3" fill="#fff"/><path d="M0 12c0-3.5 2.5-5 5.5-5s5.5 1.5 5.5 5z" fill="#fff"/></svg>Login
  </a>
</header>

<section class="hero">
  <h1>INVOICE<br>BILLABLE HOURS</h1>
  <ul class="hero-list">
    <li><svg width="18" height="18" viewBox="0 0 18 18"><circle cx="9" cy="9" r="9" fill="#7bbf3e"/><path d="M8 5l4 4-4 4" stroke="#fff" stroke-width="2" fill="none"/></svg>Automated invoicing</li>
    <li><svg width="18" height="18" viewBox="0 0 18 18"><circle cx="9" cy="9" r="9" fill="#7bbf3e"/><path d="M8 5l4 4-4 4" stroke="#fff" stroke-width="2" fill="none"/></svg>based on your time tracking/planning</li>
  </ul>
  <p class="hero-text">All your billable hours are just as valuable whether they are planned or tracked, and every minute counts.</p>
  <a class="btn btn-hero" href="#">Start billing my time</a>
  <div class="hero-art" role="img" aria-label="Illustration of a team meeting around a table in front of a presentation board with charts"></div>
</section>

<h2 class="section-title" style="top:758px">Our Features</h2>
<div class="tabs">
  <span class="tab tab-active">Time management features</span>
  <span class="tab tab-idle">Business features</span>
</div>

<!-- Time tracking -->
<div class="blob blob-blue" style="left:116px;top:951px;width:428px;height:428px"></div>
<div class="shot" style="left:181px;top:1049px;width:417px;height:237px" role="img" aria-label="Screenshot of the time tracking list with tracked entries per project"></div>
<h3 class="feature-title" style="left:647px;top:1022px">Time tracking</h3>
<p class="feature-sub" style="left:647px;top:1097px">The key to your business growth</p>
<p class="feature-text" style="left:647px;top:1146px">Keeping yourself accountable for your billing hours improves your time management skills, boost your productivity, and this inevitably leads to a remarkable increase of incomes</p>
<a class="btn btn-more" style="left:648px;top:1257px" href="#">Learn more</a>

<!-- To-do -->
<h3 class="feature-title" style="left:110px;top:1490px">To-do list</h3>
<p class="feature-sub" style="left:110px;top:1566px">Get more results per unit of time</p>
<p class="feature-text" style="left:110px;top:1616px">You know exactly what you need to do next and see clearly how your plans turn into reality. The motivators that will increase your daily productivity</p>
<a class="btn btn-more" style="left:114px;top:1727px" href="#">Learn more</a>
<div class="blob blob-green" style="left:860px;top:1500px;width:230px;height:270px"></div>
<div class="todo">
  <div class="todo-head"><span>This week to-do items</span><span>To-do list &#8599;</span></div>
  <div class="todo-item bar-red"><b>Velmora P10</b><br>Velmora/Marketing<br>Develop graphics<br>Planned: 03/01/21 15:00<span class="chk"></span></div>
  <div class="todo-item bar-orange"><b>Korvane 10</b><br>Korvane/Writing<br>Social media posts<br>Planned: 03/02/21 11:00<span class="chk"></span></div>
  <div class="todo-item bar-green"><b>Drusel P0</b><br>Drusel/Programming<br>Implementing build systems<br>Planned: 03/02/21 12:30<span class="chk"></span></div>
  <div class="todo-item bar-blue"><b>Velmora P10</b><br>Velmora/Marketing<br>Develop graphics<br>Planned: 03/03/21 05:30<span class="chk"></span></div>
  <div class="todo-item bar-blue"><b>Korvane 10</b><br>Korvane/Writing<br>Article<br>Planned: 03/03/21 09:00<span class="chk"></span></div>
  <div class="pager"><span>&laquo;</span><span class="on">1</span><span>2</span><span>&raquo;</span></div>
</div>

<!-- Someday -->
<div class="blob blob-blue" style="left:116px;top:1874px;width:428px;height:428px"></div>
<div class="shot" style="left:181px;top:1985px;width:417px;height:233px" role="img" aria-label="Screenshot of the someday tasks list with activities, projects and estimates"></div>
<h3 class="feature-title" style="left:647px;top:1958px">Someday tasks</h3>
<p class="feature-sub" style="left:647px;top:2033px">Free your mind and focus on your work</p>
<p class="feature-text" style="left:647px;top:2083px">Leaving aside the things you haven't committed to yet makes you work much more focused and efficient. At the same time, make sure you don't miss out on any of your great ideas</p>
<a class="btn btn-more" style="left:648px;top:2195px" href="#">Learn more</a>

<!-- Calendar -->
<h3 class="feature-title" style="left:110px;top:2440px">Calendar</h3>
<p class="feature-sub" style="left:110px;top:2515px">Plan and Do everything at the right time</p>
<p class="feature-text" style="left:110px;top:2566px">The complete picture of your schedule allows you to be flexible with your plans, avoid overloading the day and overlapping tasks</p>
<a class="btn btn-more" style="left:114px;top:2653px" href="#">Learn more</a>
<div class="blob blob-green" style="left:840px;top:2500px;width:250px;height:250px"></div>
<div class="shot" style="left:608px;top:2451px;width:406px;height:245px" role="img" aria-label="Screenshot of the weekly calendar with colored planned tasks"></div>

<!-- How it works -->
<section class="how">
  <h2 class="section-title" style="top:72px">How it works</h2>
  <div class="how-card" style="left:110px">
    <div class="how-icon" style="background:var(--blue)"><svg width="44" height="44" viewBox="0 0 44 44" fill="none" stroke="#fff" stroke-width="2"><circle cx="22" cy="22" r="6"/><circle cx="10" cy="10" r="4"/><circle cx="34" cy="10" r="4"/><circle cx="10" cy="34" r="4"/><circle cx="34" cy="34" r="4"/><path d="M13 13l5 5M31 13l-5 5M13 31l5-5M31 31l-5-5"/></svg></div>
    <h3>Determined people</h3>
    <p>Easily keep your goals in sight, carefully plan your actions and focus on fulfilling all your big dreams. Use your time wisely and enjoy the success.</p>
  </div>
  <div class="how-card" style="left:448px">
    <div class="how-icon" style="background:var(--green)"><svg width="44" height="44" viewBox="0 0 44 44" fill="none" stroke="#fff" stroke-width="2"><rect x="12" y="6" width="22" height="28" rx="2"/><path d="M17 14h12M17 20h12M17 26h8"/><circle cx="12" cy="34" r="5"/></svg></div>
    <h3>Freelancers</h3>
    <p>Quelvano has all the tools you need to improve your productivity while saving time and energy. Enjoy your daily achievements and thrive.</p>
  </div>
  <div class="how-card" style="left:785px">
    <div class="how-icon" style="background:var(--blue)"><svg width="44" height="44" viewBox="0 0 44 44" fill="none" stroke="#fff" stroke-width="2"><circle cx="20" cy="14" r="6"/><path d="M8 34c0-7 5-11 12-11s12 4 12 11z"/><rect x="26" y="26" width="12" height="10"/><circle cx="34" cy="10" r="4"/></svg></div>
    <h3>Small business owners</h3>
    <p>Time management streamlines the way you work and let you focus on growing your business. This brings more income and higher profits.</p>
  </div>
</section>

<!-- Extra features -->
<h2 class="section-title" style="top:3586px">Extra features</h2>
<p class="extra-intro">Lorem ipsum dolor sit amet, consectetur adipiscing elit, sed do eiusmod tempor incididunt ut labore et dolore magna aliqua. Ut enim ad minim veniam, quis nostrud exercitation ullamco laboris nisi ut aliquip ex ea commodo consequat. Duis aute irure dolor in reprehenderit in voluptate velit esse cillum dolore eu fugiat nulla pariatur.</p>

<div class="art" style="left:110px;top:3817px;width:467px;height:350px;border-radius:18px;background:linear-gradient(160deg,#e6f0fb 0%,#d3e4f7 60%,#eef6e6 100%)" role="img" aria-label="Illustration of people reviewing a large checklist document with a magnifier and a security shield"></div>
<h3 class="extra-title" style="left:648px;top:3806px">Someday tasks</h3>
<p class="extra-text" style="left:648px;top:3884px">Lorem ipsum dolor sit amet, consectetur adipiscing elit, sed do eiusmod tempor incididunt ut labore et dolore magna aliqua. Ut enim ad minim veniam, quis nostrud exercitation ullamco laboris nisi ut aliquip ex ea commodo consequat.</p>
<p class="extra-text" style="left:648px;top:4006px">Lorem ipsum dolor sit amet, consectetur adipiscing elit, sed do eiusmod tempor incididunt ut labore et dolore magna aliqua. Ut enim ad minim veniam, quis nostrud.</p>
<a class="btn btn-more" style="left:648px;top:4124px" href="#">Learn more</a>

<h3 class="extra-title" style="left:110px;top:4254px">Reports</h3>
<p class="extra-text" style="left:110px;top:4333px">Lorem ipsum dolor sit amet, consectetur adipiscing elit, sed do eiusmod tempor incididunt ut labore et dolore magna aliqua. Ut enim ad minim veniam, quis nostrud exercitation ullamco laboris nisi ut aliquip ex ea commodo consequat.</p>
<p class="extra-text" style="left:110px;top:4454px">Lorem ipsum dolor sit amet, consectetur adipiscing elit, sed do eiusmod tempor incididunt ut labore et dolore magna aliqua. Ut enim ad minim veniam, quis nostrud.</p>
<a class="btn btn-more" style="left:110px;top:4573px;width:130px" href="#">Learn more</a>
<div class="art" style="left:625px;top:4263px;width:463px;height:360px;border-radius:50%;background:linear-gradient(150deg,#eef1f5 0%,#e2e8f0 55%,#fbe7b5 100%)" role="img" aria-label="Illustration of a person working at a computer showing a report, with a potted plant"></div>

<footer class="site-footer">
  <div class="foot-brand"><span class="brand-name">Quelvano</span><span class="brand-dot"></span></div>
  <div class="social"><span></span><span></span><span></span><span></span></div>
  <div class="foot-col" style="left:361px"><h4>Time management</h4><ul><li>Time tracking</li><li>To Do list</li><li>Someday tasks</li><li>Calendar</li></ul></div>
  <div class="foot-col" style="left:561px"><h4>Business features</h4><ul><li>Estimates/Quotations</li><li>Project breakdown</li><li>Detailed timesheet</li><li>Invoicing</li></ul></div>
  <div class="foot-col" style="left:771px"><h4>Productivity</h4><ul><li>Continous workflow</li><li>Planned Day vs Real Day</li><li>Gridwell exports</li><li>About us</li></ul></div>
  <div class="foot-col" style="left:996px"><h4>Resources</h4><ul><li>Blog</li><li>Blog RO</li><li>Updates</li><li>Contact us</li></ul></div>
  <div class="foot-rule"></div>
  <p class="foot-bottom" style="left:480px">&copy; 2023 QUELVANO &nbsp;|&nbsp; All Rights Reserved</p>
  <p class="foot-bottom" style="left:846px">PRIVACY POLICY &nbsp;&nbsp;|&nbsp;&nbsp; TERMS &amp; CONDITIONS</p>
  <p class="foot-bottom" style="left:1133px">C45</p>
</footer>

</body>
</html>
```